Lumo Brew Premium Matcha brand Label

This is a label design project for a luxury tea brand. Feel free to be creative within the guidelines.
Attached to this project is a document called “Private Label Design Requirements” with the design guidelines and template. There is another document called "Lumo Brew Packaging Instructions" this has more details necessary to stick to the guidelines in the first document.

I have also attached the certifications to be included as well as different variations of the logo for you to use.

If you have any questions, I am here.
Updates

Target Market(s)

Young, active, fun, enjoy the finer things

```html
<!DOCTYPE html>
<html lang="en">
<head>
<meta charset="utf-8">
<title>Lumo Brew Premium Matcha Label</title>
<link rel="stylesheet" href="https://fonts.googleapis.com/css2?family=Great+Vibes&family=Roboto:wght@400;500;700&display=swap">
<style>
  :root {
    --page: #ffffff;
    --band: #161616;
    --band-light: #262626;
    --tab: #e5197f;
    --green: #7ccf5a;
    --green-deep: #4fae3a;
    --white: #ffffff;
    --muted: #d9d9d9;
    --stock: #ffffff;
    --edge: #c9c9c9;
  }
  * { box-sizing: border-box; margin: 0; padding: 0; }
  html, body { width: 1200px; height: 1200px; overflow: hidden; background: var(--page); }
  body { position: relative; font-family: "Roboto", Arial, sans-serif; color: var(--white); }

  .label {
    position: absolute; left: 20px; top: 500px; width: 1160px; height: 200px;
    background: var(--stock); border: 1px solid var(--edge);
  }
  .tab { position: absolute; width: 38px; height: 20px; background: var(--tab); }
  .tab--tl { left: 0; top: 0; } .tab--bl { left: 0; bottom: 0; }
  .tab--tr { right: 0; top: 0; } .tab--br { right: 0; bottom: 0; }

  .band {
    position: absolute; left: 45px; right: 45px; top: 20px; bottom: 20px;
    background: radial-gradient(ellipse at 50% 40%, var(--band-light), var(--band) 70%);
    overflow: hidden;
  }
  .store-strip {
    position: absolute; right: 0; top: 0; bottom: 0; width: 54px; background: var(--stock);
  }
  .store-strip span {
    position: absolute; left: 12px; top: 8px; writing-mode: vertical-rl;
    font-size: 7px; color: #333;
  }

  /* left panel */
  .facts { position: absolute; left: 18px; top: 8px; width: 235px; }
  .facts-box { border: 1px solid #777; border-radius: 4px; padding: 2px 6px 3px; }
  .facts h2 { font-size: 13px; line-height: 15px; font-weight: 700; color: var(--green); border-bottom: 1px solid #777; padding-bottom: 1px; }
  .facts p { font-size: 5.5px; line-height: 7px; color: var(--muted); border-bottom: 1px solid #444; display: flex; justify-content: space-between; }
  .facts p:last-child { border-bottom: 0; }
  .distributor { position: absolute; left: 18px; top: 114px; width: 140px; }
  .distributor .title { font-size: 11px; line-height: 12px; color: var(--green); }
  .distributor .addr { font-size: 7px; line-height: 9px; color: var(--white); margin-top: 1px; }
  .distributor .origin { font-size: 11px; line-height: 12px; color: var(--green); margin-top: 2px; }
  .seal { position: absolute; left: 165px; top: 116px; width: 34px; height: 34px; border-radius: 50%; background: var(--green-deep); border: 2px solid #2f2f2f; }

  /* centre */
  .brand { position: absolute; left: 0; right: 54px; top: 12px; text-align: center; }
  .brand-mark {
    display: inline-flex; align-items: center; gap: 6px;
    background: #000; padding: 8px 10px;
  }
  .brand-dot { width: 12px; height: 12px; border-radius: 50%; background: var(--white); }
  .brand-name { font-size: 14px; font-weight: 500; color: var(--white); }
  .tagline { font-family: "Great Vibes", cursive; font-size: 18px; color: var(--green); margin-top: 10px; }
  .product { font-size: 20px; font-weight: 500; color: var(--white); margin-top: 2px; }
  .net { font-size: 9px; font-weight: 500; color: var(--green); margin-top: 16px; }

  /* right panel */
  .details { position: absolute; left: 790px; top: 6px; width: 240px; }
  .details h3 { font-size: 13px; line-height: 15px; font-weight: 400; color: var(--white); }
  .details .ingredient { font-size: 8px; line-height: 10px; color: var(--white); margin-bottom: 5px; }
  .details ul { list-style: none; margin-top: 2px; }
  .details li { font-size: 8px; line-height: 12px; color: var(--white); }
  .details li::before { content: "• "; }
  .certs { position: absolute; left: 790px; top: 118px; display: flex; gap: 8px; align-items: center; }
  .cert { width: 28px; height: 28px; background: #3a7bc8; border-radius: 4px; }
  .cert--round { border-radius: 50%; background: #2f8a3a; border: 2px solid var(--white); }
  .keep { font-size: 9px; line-height: 11px; color: var(--white); margin-left: 10px; }
</style>
</head>
<body>
  <div class="label">
    <div class="tab tab--tl"></div><div class="tab tab--bl"></div>
    <div class="tab tab--tr"></div><div class="tab tab--br"></div>

    <div class="band">
      <section class="facts">
        <div class="facts-box">
          <h2>Nutritional Facts</h2>
          <p><span>Serving Size 1 Scoop</span></p>
          <p><span>Servings Per Container 30</span></p>
          <p><span>Amount Per Serving</span><span>%DV</span></p>
          <p><span>Calories 0</span></p>
          <p><span>Total Fat 0g</span><span>0%</span></p>
          <p><span>Sodium 0mg</span><span>0%</span></p>
          <p><span>Total Carbs 0g</span><span>0%</span></p>
          <p><span>Protein 0g</span><span>0%</span></p>
          <p><span>Caffeine 35mg</span></p>
        </div>
      </section>
      <section class="distributor">
        <div class="title">Distributed by :</div>
        <div class="addr">Lumo Brew Co, 45 Maple Ln. Springfield<br>United States</div>
        <div class="origin">PRODUCT OF JAPAN</div>
      </section>
      <div class="seal" role="img" aria-label="Certification seal"></div>

      <section class="brand">
        <div class="brand-mark"><span class="brand-dot"></span><span class="brand-name">Lumo Brew</span></div>
        <div class="tagline">Premium Organic Ceremonial Matcha</div>
        <div class="product">Japanese Tea</div>
        <div class="net">Net Wt: 30g</div>
      </section>

      <section class="details">
        <h3>Ingredients</h3>
        <div class="ingredient">Organic Japanese Matcha Green Tea</div>
        <h3>Instructions to use</h3>
        <ul>
          <li>2 tsp of Matcha</li>
          <li>2oz of Water (170-180 degrees F)</li>
          <li>Whisk in a W formation until frothy</li>
          <li>Sweeten to taste</li>
        </ul>
      </section>
      <div class="certs">
        <div class="cert" role="img" aria-label="Non-GMO certification badge"></div>
        <div class="cert cert--round" role="img" aria-label="Organic certification badge"></div>
        <div class="keep">KEEP REFRIGERATED<br>FOR QUALITY</div>
      </div>

      <div class="store-strip"><span>Store in a cool dry place</span></div>
    </div>
  </div>
</body>
</html>
```